Captivating packaging design for sports company.

We need a packaging design that encompasses our resistance bands workout set. Our focus is quality, convenience, and versatility. The design should be tailored to our broad array of customer across all paths. We would like the packaging to reflect our brand and product features such as: the LBS(weight) listed on each of the bands, convenience for travel and at home, highest quality, for all fitness levels, and free eBook. We'd also like to include a couple of our reviews on the packaging. Please refer to our listing on Varnel for additional information https://www.shopvarnel.com/Brisket-Athletic-Resistance-Workout-Carrying/dp/Q7ZK4MRT2X/ref=sr_1_1?ie=UTF8&qid=1470453588&sr=8-1&keywords=brisket+athletic+resistance+bands
Please reach out with additional questions for any further details. Thank you.
Target Market(s)
Sports, fitness, and health enthusiasts of all ages.
Industry/Entity Type
It Company
Look and feel
Each slider illustrates characteristics of the customer's brand and the style your logo design should communicate.

```html
<!DOCTYPE html>
<html lang="en">
<head>
<meta charset="utf-8">
<title>Brisket Athletic – Resistance Band Package</title>
<link rel="stylesheet" href="https://fonts.googleapis.com/css2?family=Open+Sans:ital,wght@0,300;0,400;0,600;0,700;1,300&display=swap">
<style>
  :root {
    --backdrop: #e4e4e4;
    --face: #ededed;
    --panel-dark: #2f2f2f;
    --brand-red: #7a1a1c;
    --band-red: #6e1418;
    --band-orange: #b5461a;
    --band-yellow: #c9b118;
    --text-light: #ffffff;
    --text-muted: #c4c4c4;
    --figure-dark: #2a2a2a;
    --figure-mid: #777777;
  }
  html, body {
    margin: 0;
    padding: 0;
    width: 1200px;
    height: 900px;
    overflow: hidden;
    background: var(--backdrop);
    font-family: "Open Sans", Arial, sans-serif;
  }
  .package-front {
    position: absolute;
    left: 289px;
    top: 127px;
    width: 622px;
    height: 645px;
    background: var(--face);
    overflow: hidden;
  }
  .package-shapes {
    position: absolute;
    inset: 0;
  }
  .brand {
    position: absolute;
    left: 32px;
    top: 62px;
    display: flex;
    align-items: center;
    gap: 12px;
  }
  .brand-dot {
    width: 46px;
    height: 46px;
    border-radius: 50%;
    background: var(--brand-red);
  }
  .brand-name {
    color: var(--brand-red);
    font-weight: 700;
    font-size: 27px;
    line-height: 1.02;
    letter-spacing: 0.5px;
    text-transform: uppercase;
  }
  .product-title {
    position: absolute;
    left: 330px;
    top: 36px;
    margin: 0;
    color: var(--text-light);
    font-weight: 400;
    font-size: 33px;
    line-height: 1.18;
  }
  .product-sub {
    position: absolute;
    left: 330px;
    top: 126px;
    width: 112px;
    padding-top: 10px;
    border-top: 1px solid var(--text-muted);
    color: var(--text-muted);
    font-style: italic;
    font-weight: 300;
    font-size: 17px;
    line-height: 1.72;
  }
  .athlete-photo {
    position: absolute;
    left: 78px;
    top: 232px;
    width: 225px;
    height: 352px;
    background: linear-gradient(180deg, var(--figure-dark) 0%, var(--figure-dark) 70%, var(--figure-mid) 100%);
    opacity: 0.85;
  }
</style>
</head>
<body>
  <main class="package-front">
    <svg class="package-shapes" width="622" height="645" viewBox="0 0 622 645" aria-hidden="true">
      <defs>
        <linearGradient id="heat-band" x1="1" y1="0" x2="0" y2="1">
          <stop offset="0" stop-color="var(--band-red)"/>
          <stop offset="0.45" stop-color="var(--band-orange)"/>
          <stop offset="1" stop-color="var(--band-yellow)"/>
        </linearGradient>
      </defs>
      <polygon class="heat-band" points="565,0 622,0 622,645 205,645" fill="url(#heat-band)"/>
      <polygon class="title-panel" points="316,22 545,22 316,390" fill="var(--panel-dark)"/>
      <rect class="edge-stripe-left" x="0" y="0" width="8" height="420" fill="var(--brand-red)"/>
      <rect class="edge-stripe-right" x="612" y="270" width="10" height="350" fill="var(--band-red)"/>
    </svg>

    <div class="brand">
      <span class="brand-dot"></span>
      <span class="brand-name">Brisket<br>Athletic</span>
    </div>

    <h1 class="product-title">Resistance<br>Band</h1>
    <p class="product-sub">Workout Set<br>with<br>Door<br>Anchor</p>

    <div class="athlete-photo" role="img" aria-label="Photo of an athlete in a lunge pulling a resistance band, with her reflection on the floor"></div>
  </main>
</body>
</html>
```